Trucking company needs business card design

New trucking company needs fresh ideas on a business card. Contracted exclusively to ParcelWing, can incorporate their colors or style, but not necessary.
Calder Haulage, Inc (with or without the Inc.)
Dale Whitcombe, CEO
801-555-0147
PO BOX 372
Lehi, UT
Updates

Need to add my email address to the card--calderhaulageinc@roadmail.example

Industry/Entity Type

Trucking Company

```html
<!DOCTYPE html>
<html lang="en">
<head>
<meta charset="utf-8">
<title>Calder Haulage, Inc – Business Card</title>
<link href="https://fonts.googleapis.com/css2?family=Open+Sans:wght@400;600;700&display=swap" rel="stylesheet">
<style>
  :root {
    --stage: #2b2b2d;
    --card-light: #ffffff;
    --card-shade: #e2e3e5;
    --brand-blue: #1a8ccc;
    --accent-red: #e0402a;
    --accent-orange: #ef5a24;
    --text-white: #ffffff;
  }
  * { margin: 0; padding: 0; box-sizing: border-box; }
  html, body {
    width: 1200px; height: 1000px; overflow: hidden;
    background: var(--stage);
    font-family: "Open Sans", Arial, sans-serif;
  }
  .stage {
    width: 1200px; height: 1000px;
    display: flex; flex-direction: column; align-items: center; justify-content: center;
    gap: 60px;
  }
  .card {
    position: relative;
    width: 700px; height: 400px;
    border-radius: 34px;
    overflow: hidden;
    background: radial-gradient(ellipse at 50% 40%, var(--card-light) 0%, #f1f2f3 45%, var(--card-shade) 100%);
    box-shadow: 0 18px 40px rgba(0,0,0,.45);
  }
  .band {
    position: absolute; left: 0; right: 0; bottom: 0;
    background: var(--brand-blue);
    border-top: 6px solid var(--accent-red);
  }
  .card--front .band { height: 92px; display: flex; align-items: center; justify-content: center; }
  .card--back .band { height: 170px; }
  .brand {
    position: absolute; left: 0; right: 0;
    display: flex; align-items: center; justify-content: center; gap: 16px;
  }
  .card--front .brand { top: 130px; }
  .card--back .brand { top: 80px; }
  .brand__dot {
    width: 38px; height: 38px; border-radius: 50%;
    background: var(--brand-blue);
  }
  .brand__name {
    font-weight: 700; font-size: 44px; letter-spacing: 2px;
    text-transform: uppercase; color: var(--brand-blue);
  }
  .website {
    color: var(--text-white); font-size: 22px; letter-spacing: .5px;
  }
  .contact {
    position: absolute; left: 44px; right: 36px; top: 26px; bottom: 22px;
    display: flex; justify-content: space-between; align-items: stretch;
    gap: 20px;
    color: var(--text-white);
    white-space: nowrap;
  }
  .person {
    display: flex; flex-direction: column; justify-content: flex-end;
  }
  .person__line { line-height: 1.2; }
  .person__name { font-size: 28px; font-weight: 700; }
  .person__role { font-size: 22px; font-weight: 400; margin-left: 8px; }
  .person__address { font-size: 21px; margin-top: 4px; padding-left: 44px; line-height: 1.3; }
  .reach { list-style: none; display: flex; flex-direction: column; gap: 8px; }
  .reach__item { display: flex; align-items: center; gap: 10px; font-size: 18px; }
  .reach__icon { width: 20px; height: 20px; flex: none; }
</style>
</head>
<body>
<main class="stage">
  <section class="card card--front" aria-label="Card front">
    <div class="brand">
      <span class="brand__dot"></span>
      <span class="brand__name">Calder Haulage Inc</span>
    </div>
    <div class="band">
      <span class="website">www.calderhaulage.example</span>
    </div>
  </section>

  <section class="card card--back" aria-label="Card back">
    <div class="brand">
      <span class="brand__dot"></span>
      <span class="brand__name">Calder Haulage Inc</span>
    </div>
    <div class="band">
      <div class="contact">
        <div class="person">
          <p class="person__line"><span class="person__name">Dale Whitcombe</span><span class="person__role">CEO</span></p>
          <p class="person__address">PO BOX 372 Lehi, UT</p>
        </div>
        <ul class="reach">
          <li class="reach__item">
            <svg class="reach__icon" viewBox="0 0 24 24" aria-hidden="true">
              <circle cx="12" cy="12" r="11" fill="var(--accent-orange)"/>
              <path d="M8.5 6.5l2 2.2-1.2 1.5c.8 1.6 2 2.8 3.6 3.6l1.5-1.2 2.2 2-1.4 1.9c-3.9-.4-7.1-3.6-7.6-7.6z" fill="#fff"/>
            </svg>
            <span>801-555-0147</span>
          </li>
          <li class="reach__item">
            <svg class="reach__icon" viewBox="0 0 24 24" aria-hidden="true">
              <circle cx="12" cy="12" r="11" fill="var(--accent-orange)"/>
              <rect x="6" y="8" width="12" height="8.5" rx="1" fill="#fff"/>
              <path d="M6.4 8.6L12 13l5.6-4.4" fill="none" stroke="var(--accent-orange)" stroke-width="1.3"/>
            </svg>
            <span>calderhaulageinc@roadmail.example</span>
          </li>
        </ul>
      </div>
    </div>
  </section>
</main>
</body>
</html>
```